International recycling company needs urgently logo and dossier cover design

We have a logo, but we need it valid to print (pdf, CMYK, 300dpi).
Attached you will find what we have.
Besides, we need a cover design for a corporate dossier, with the logo and corporate colours, nothing else.

Industry/Entity Type

Recycling

Colors
0492cd
32a6d7
85cae6
cde9f5

Requirements
Must have
• Flat color soft blue background.

```html
<!DOCTYPE html>
<html lang="en">
<head>
<meta charset="utf-8">
<title>OreLink – Dossier Cover</title>
<link href="https://fonts.googleapis.com/css2?family=EB+Garamond:wght@500&display=swap" rel="stylesheet">
<style>
  :root {
    --page-bg: #ffffff;
    --cover-blue: #a9d3fb;
    --globe-light: #f4f9ff;
    --globe-mid: #bcdcfb;
    --globe-deep: #8fbdeb;
    --brand-blue: #0a5cbf;
  }
  html, body {
    margin: 0;
    padding: 0;
    width: 1200px;
    height: 1000px;
    overflow: hidden;
    background: var(--page-bg);
  }
  .canvas {
    position: relative;
    width: 1200px;
    height: 1000px;
  }
  .dossier-cover {
    position: absolute;
    left: 280px;
    top: 104px;
    width: 640px;
    height: 790px;
    background: var(--cover-blue);
    overflow: hidden;
  }
  .globe-illustration {
    position: absolute;
    left: 0;
    top: 0;
    width: 640px;
    height: 790px;
  }
  .brand-mark {
    position: absolute;
    left: 451px;
    top: 620px;
    width: 128px;
    height: 128px;
    z-index: 1;
  }
  .brand-lockup {
    position: absolute;
    right: 194px;
    top: 656px;
    z-index: 2;
    text-align: right;
    white-space: nowrap;
    color: var(--brand-blue);
    font-family: "EB Garamond", Garamond, serif;
    font-weight: 500;
  }
  .brand-name {
    margin: 0;
    font-size: 40px;
    line-height: 1;
    letter-spacing: 0.5px;
  }
  .brand-tagline {
    margin: 8px 0 0;
    font-size: 17px;
    line-height: 1;
  }
</style>
</head>
<body>
  <main class="canvas">
    <section class="dossier-cover">
      <svg class="globe-illustration" viewBox="0 0 640 790" role="img" aria-label="Large soft-blue globe illustration showing the Americas and Africa">
        <defs>
          <radialGradient id="globeShade" cx="0.3" cy="0.3" r="0.8">
            <stop offset="0" stop-color="var(--globe-light)"/>
            <stop offset="0.5" stop-color="var(--globe-mid)"/>
            <stop offset="1" stop-color="var(--globe-deep)"/>
          </radialGradient>
          <linearGradient id="globeFade" x1="0" y1="0" x2="0" y2="1">
            <stop offset="0.6" stop-color="#fff" stop-opacity="1"/>
            <stop offset="1" stop-color="#fff" stop-opacity="0"/>
          </linearGradient>
          <mask id="fadeMask">
            <rect x="0" y="0" width="640" height="560" fill="url(#globeFade)"/>
          </mask>
        </defs>
        <circle cx="250" cy="290" r="290" fill="url(#globeShade)" mask="url(#fadeMask)"/>
      </svg>

      <svg class="brand-mark" viewBox="0 0 128 128" aria-hidden="true">
        <defs>
          <radialGradient id="markShade" cx="0.35" cy="0.3" r="0.75">
            <stop offset="0" stop-color="#ffffff"/>
            <stop offset="1" stop-color="#7fb2e6"/>
          </radialGradient>
        </defs>
        <circle cx="64" cy="64" r="63" fill="url(#markShade)"/>
      </svg>

      <div class="brand-lockup">
        <p class="brand-name">OreLink</p>
        <p class="brand-tagline">Metals Management Company</p>
      </div>
    </section>
  </main>
</body>
</html>
```